Wochen Speiseplan
Zielgruppe
Hospiz
Aufgabenstellung
Wir brauchen für unser Hospiz einen Wochenspeiseplan. Es soll eine Powerpointseite im A4 Format erstellt werden. Wir brauchen 4 unterschiedliche Seiten - für jede Jahreszeit einen Entwurf. Der Speiseplan soll von uns selbst ausgefüllt werden können.
Inhalte: Montag - Sonntag jeweils Mittag- und Abendessen. (Aufgebaut wie ein Stundenplan.). Möglichst große Schriftgröße. In der Fußnote bitte: "Änderungen vorbehalten schreiben". Das ganze soll professionell, aber dennoch liebevoll gestaltet sein. Es soll unseren Bewohnern "Liust machen" draufzuschauen. Der Plan wird jede Woche neu ausgefüllt, ausgedruckt und laminiert. Sollte also einfach zu handhaben sein.
Das Hospiz lebt von Spenden, daher bitte nicht zu aufwendig, dafür aber bezahlbar machen.

```html
<!DOCTYPE html>
<html lang="de">
<head>
<meta charset="utf-8">
<title>Wochenspeiseplan</title>
<link rel="stylesheet" href="https://fonts.googleapis.com/css2?family=Chewy&family=Noto+Sans:ital,wght@0,400;0,700;1,700&family=Noto+Serif:wght@400&display=swap">
<style>
  :root {
    --bg-light: #d88a5e;
    --bg-dark: #b9653c;
    --banner: #7d0019;
    --banner-ornament: #9a2a3a;
    --header: #c2380b;
    --header-text: #eba487;
    --row-dark: #e6b6b3;
    --row-light: #f2dbd9;
    --grid: #f6e6e4;
    --text: #1d1d1d;
    --white: #ffffff;
  }
  * { box-sizing: border-box; margin: 0; padding: 0; }
  html, body { width: 1200px; height: 900px; overflow: hidden; }
  body { position: relative; font-family: "Noto Sans", sans-serif; color: var(--text); }

  .backdrop {
    position: absolute; inset: 0;
    background: radial-gradient(ellipse at 30% 40%, var(--bg-light) 0%, var(--bg-dark) 100%);
  }
  .banner { position: absolute; left: 0; top: 0; width: 1200px; height: 260px; }
  .banner-ornament {
    position: absolute; right: 0; top: 0; width: 160px; height: 140px;
    background: radial-gradient(circle at 70% 40%, var(--banner-ornament) 0%, transparent 70%);
  }
  .title {
    position: absolute; left: 278px; top: 32px;
    font-family: "Chewy", cursive; font-size: 98px; line-height: 1;
    color: var(--white); letter-spacing: 1px;
  }
  .tagline {
    position: absolute; left: 440px; top: 178px;
    font-family: "Noto Serif", serif; font-size: 30px; color: var(--white);
    transform: rotate(-7deg); transform-origin: left bottom; white-space: nowrap;
  }

  .menu {
    position: absolute; left: 38px; top: 260px; width: 1127px;
    border-collapse: collapse; table-layout: fixed;
  }
  .menu col.day { width: 179px; }
  .menu col.lunch { width: 466px; }
  .menu col.dinner { width: 482px; }
  .menu th {
    height: 65px; background: var(--header); color: var(--header-text);
    font-style: italic; font-weight: 700; font-size: 28px; text-align: left;
    padding-left: 15px; letter-spacing: 1px;
  }
  .menu td {
    height: 73px; vertical-align: top; padding: 10px 12px 0;
    font-size: 21px; line-height: 1.3; border-left: 2px solid var(--grid);
  }
  .menu td:first-child { border-left: none; font-weight: 700; font-style: italic; font-size: 22px; }
  .menu tr:nth-child(odd) td { background: var(--row-dark); }
  .menu tr:nth-child(even) td { background: var(--row-light); }
  .menu tbody tr + tr td { border-top: 2px solid var(--grid); }

  .footnote {
    position: absolute; right: 18px; top: 852px;
    font-size: 19px; font-weight: 700; font-style: italic;
  }
</style>
</head>
<body>
  <div class="backdrop" role="img" aria-label="Warmer orange-brauner Hintergrund mit verschnörkelten Ornamenten"></div>

  <svg class="banner" viewBox="0 0 1200 260" aria-hidden="true">
    <polygon points="238,0 1200,0 1200,158 250,247" fill="var(--banner)"/>
  </svg>
  <div class="banner-ornament" role="img" aria-label="Dekoratives Rankenornament"></div>

  <h1 class="title">Wochenspeiseplan</h1>
  <p class="tagline">Wir wünschen einen guten Appetit!</p>

  <table class="menu">
    <colgroup><col class="day"><col class="lunch"><col class="dinner"></colgroup>
    <thead>
      <tr><th></th><th>Mittagessen</th><th>Abendessen</th></tr>
    </thead>
    <tbody>
      <tr><td>Montag</td><td>Spaghetti Bolognese</td><td>Gemüsepfanne mit Hähnchenbrust</td></tr>
      <tr><td>Dienstag</td><td>Chicken Wrap mit buntem Salat<br>und Guacamole</td><td>Gebratener Seehecht in Ei-Hülle<br>dazu Kartoffelpüree</td></tr>
      <tr><td>Mittwoch</td><td>Milchreis mit Zucker/Zimt<br>und Kirschkompott</td><td>Frikadelle schwäbische Art auf<br>Kräuterspätzle</td></tr>
      <tr><td>Donnerstag</td><td>Nudeleintopf mit Geflügelfleisch</td><td>Gegrillte Schweinshaxe</td></tr>
      <tr><td>Freitag</td><td>Germknödel mit Pflaumenmusfüllung</td><td>Nudel-Schinken-Gratin dazu<br>gemischter Salat</td></tr>
      <tr><td>Samstag</td><td>3 gekochte Eier mit Senfsoße und<br>Kartoffeln</td><td>Kartoffelrösti mit Tomaten-Schnittlauch-<br>Quark</td></tr>
      <tr><td>Sonntag</td><td>Linseneintopf mit Bockwurst,<br>Fladenbrot</td><td>Kochklopse Königsberger Art mit<br>Kartoffeln/Reis</td></tr>
    </tbody>
  </table>

  <p class="footnote">Änderungen vorbehalten</p>
</body>
</html>
```